Tomasi's Pizzeria BOGO Promotion Pizza Flyer (Huron)

Pizzeria flyer promoting "under new management" and then the main point for this flyer is our Buy One Get One Free promotion on our pizzas (disclaimer: not valid for Jr Family Crust or Family Pizzas)(we reserve the right to cancel this promotion at any time)
This promotion has no limit and can be carryout or delivery. No coupon needed.
Looking for a fun bright flyer with our logo colors

Requirements
Must have
• Store Info
• 287 Marwick Rd. E
• Millbrook, OH
• 419-562-3870
• Open at 4pm Daily!

```html
<!DOCTYPE html>
<html lang="en">
<head>
<meta charset="utf-8">
<title>Tomasi's Pizzeria – Buy One Get One Free</title>
<link href="https://fonts.googleapis.com/css2?family=Oswald:wght@400;500;600&family=Roboto:wght@400;500;700&family=Roboto+Condensed:ital,wght@1,700&display=swap" rel="stylesheet">
<style>
  :root {
    --wood-dark: #2a1a12;
    --wood-mid: #4a3022;
    --wood-light: #5e3d2b;
    --band: rgba(20, 12, 8, 0.45);
    --ribbon: #f2b51c;
    --ribbon-shade: #c98d0d;
    --ink-dark: #2a1a12;
    --text-light: #f4efe9;
    --text-soft: #d9d2cb;
    --brand-red: #c8202a;
    --pizza-crust: #b9772f;
    --pizza-top: #d99a42;
  }
  * { margin: 0; padding: 0; box-sizing: border-box; }
  html, body { width: 816px; height: 1200px; overflow: hidden; background: #e6e6e6; }
  .flyer {
    position: relative;
    width: 816px;
    height: 1200px;
    overflow: hidden;
    background:
      repeating-linear-gradient(90deg, rgba(0,0,0,0) 0 134px, rgba(0,0,0,0.35) 134px 136px),
      linear-gradient(100deg, var(--wood-dark) 0%, var(--wood-mid) 35%, var(--wood-light) 55%, var(--wood-mid) 75%, var(--wood-dark) 100%);
    font-family: "Roboto", Arial, sans-serif;
    color: var(--text-light);
  }
  .hero-photo {
    position: absolute;
    left: 0; top: 0;
    width: 816px; height: 290px;
    background: radial-gradient(ellipse at 55% 30%, var(--pizza-top) 0%, var(--pizza-crust) 55%, #3b2416 85%, var(--wood-dark) 100%);
  }
  .ribbon {
    position: absolute;
    left: -20px; top: 282px;
    width: 600px; height: 66px;
    background: var(--ribbon);
    transform: rotate(-5deg);
    transform-origin: left center;
    box-shadow: 0 6px 10px rgba(0,0,0,0.4);
    display: flex; align-items: center;
    padding-left: 70px;
    font-family: "Roboto Condensed", Arial, sans-serif;
    font-style: italic; font-weight: 700;
    font-size: 36px;
    color: var(--ink-dark);
  }
  .ribbon::after {
    content: "";
    position: absolute; right: -28px; top: 0;
    border-style: solid;
    border-width: 33px 0 33px 28px;
    border-color: var(--ribbon) transparent var(--ribbon) var(--ribbon-shade);
  }
  .brand {
    position: absolute;
    left: 40px; top: 480px;
    width: 280px;
    display: flex; flex-direction: column; align-items: center; gap: 18px;
  }
  .brand-mark {
    width: 170px; height: 170px; border-radius: 50%;
    background: var(--brand-red);
  }
  .brand-name {
    font-family: "Oswald", Arial, sans-serif;
    font-weight: 600; font-size: 40px; line-height: 1.05;
    text-align: center; color: var(--text-light);
  }
  .offer {
    position: absolute;
    left: 345px; top: 415px;
    width: 410px; height: 320px;
    transform: rotate(-8deg);
    border: 4px dashed var(--text-soft);
    padding: 24px 30px;
    font-family: "Oswald", Arial, sans-serif;
    text-transform: uppercase;
    line-height: 0.98;
    text-align: center;
    color: var(--text-light);
    text-shadow: 0 4px 6px rgba(0,0,0,0.5);
  }
  .offer-line { display: block; font-weight: 400; font-size: 76px; letter-spacing: 2px; }
  .offer-free { display: block; font-weight: 600; font-size: 124px; letter-spacing: 4px; color: #ececec; }
  .terms {
    position: absolute;
    left: 110px; right: 110px; top: 830px;
    text-align: center;
    font-size: 32px; line-height: 1.3;
    color: var(--text-light);
  }
  .store-info {
    position: absolute;
    left: 0; right: 0; top: 975px; height: 170px;
    background: var(--band);
    text-align: center;
    padding-top: 20px;
  }
  .store-address { font-size: 28px; font-weight: 500; }
  .store-phone { font-size: 54px; font-weight: 700; margin: 2px 0; letter-spacing: 1px; }
  .store-hours { font-size: 28px; font-weight: 500; }
  .disclaimer {
    position: absolute;
    left: 0; right: 0; bottom: 0; height: 55px;
    background: rgba(10, 6, 4, 0.6);
    display: flex; align-items: center; justify-content: center;
    font-size: 14px; color: var(--text-soft);
  }
</style>
</head>
<body>
  <main class="flyer">
    <div class="hero-photo" role="img" aria-label="Photo of a deep-dish pizza with olives, peppers and mushrooms in a cast-iron pan"></div>

    <div class="ribbon">Under new management</div>

    <div class="brand">
      <div class="brand-mark"></div>
      <div class="brand-name">Tomasi's Pizzeria</div>
    </div>

    <div class="offer">
      <span class="offer-line">Buy One</span>
      <span class="offer-line">Get One</span>
      <span class="offer-free">Free</span>
    </div>

    <p class="terms">This promotion has no limit and can be carryout or delivery. No coupon needed.</p>

    <section class="store-info">
      <p class="store-address">287 Marwick Rd. E, Millbrook, OH</p>
      <p class="store-phone">(555) 562-3870</p>
      <p class="store-hours">Open at 4pm Daily!</p>
    </section>

    <p class="disclaimer">Not valid for Jr Family Crust or Family Pizzas. We reserve the right to cancel this promotion at any time.</p>
  </main>
</body>
</html>
```